Brochure design for TOVANIX clinic

We are seeking for a brochure design for new medical walk-in clinic.
The desirable design for the brochure will contain strong concept of positioning for
" convenience" of medical care in terms of access, affordability and service.
I am looking forward to having eye-catching modern design.
Updates

 I've updated the logo file to ai file

and for your reference please see our web page www.tova-nix.com
to keep consistency in terms of  color scheme  and impression

Thanks

Dear Designers,

We'd like to make the deadline earlier by Dec 17(Tuesday) 
Thank you..

Target Market(s)

Age from 20 - 50

Industry/Entity Type

Medical

Colors
f78f20
33a6d7

Requirements
Must have
• Multi-language greeting line in Korean, Chinese, Japanese and English on the cover page.

8 x11.7 sized tri-fold
Nice to have
• Please refer to our web page in order to keep consistency
www.tova-nix.com

```html
<!DOCTYPE html>
<html lang="en">
<head>
<meta charset="utf-8">
<title>TOVANIX Convenience Clinic – Tri-fold Brochure</title>
<link rel="stylesheet" href="https://fonts.googleapis.com/css2?family=Questrial&family=Montserrat:wght@400;600;700&family=Noto+Sans+KR:wght@300&family=Noto+Sans+JP:wght@400&family=Noto+Sans+SC:wght@500&display=swap">
<style>
  :root {
    --orange: #f78f20;
    --blue: #33a6d7;
    --navy: #233a5e;
    --panel-dark: #3a3a3c;
    --text-light: #e9e9e9;
    --grey-frame: #9a9a9a;
    --grey-text: #8a8a8a;
  }
  * { margin: 0; padding: 0; box-sizing: border-box; }
  html, body { width: 1200px; height: 937px; overflow: hidden; background: #ffffff; }
  .brochure {
    position: relative; width: 1200px; height: 937px; overflow: hidden;
    font-family: "Questrial", sans-serif;
    background: linear-gradient(90deg, #ececec 0%, #fafafa 40%, #f1f1f1 100%);
  }
  .bottom-band { position: absolute; left: 0; right: 0; bottom: 0; height: 15px; background: var(--orange); }
  .fold { position: absolute; top: 0; bottom: 15px; left: 801px; width: 1px; background: rgba(0,0,0,0.08); }

  /* Experts panel */
  .experts {
    position: absolute; left: 0; top: 0; width: 399px; height: 922px; overflow: hidden;
    background: var(--panel-dark); color: var(--text-light);
    padding: 26px 33px 0 34px;
  }
  .experts-title {
    font-size: 27px; font-weight: 400; color: var(--blue);
    font-variant: small-caps; letter-spacing: 0.5px;
    padding-left: 40px; padding-bottom: 3px;
    border-bottom: 2px solid var(--orange);
  }
  .expert { margin-top: 19px; font-size: 12px; line-height: 14.7px; text-align: justify; }
  .expert + .expert { margin-top: 26px; }
  .expert-card { float: left; width: 131px; margin-right: 0; }
  .expert-photo { width: 94px; height: 115px; background: linear-gradient(160deg, #3f5f86, #24324a 60%, #c9a98a); }
  .expert-photo.second { background: linear-gradient(160deg, #c99c7c, #8a6b58 55%, #564436); }
  .expert-name { font-family: "Montserrat", sans-serif; font-weight: 600; color: var(--blue); font-size: 12.5px; line-height: 15px; margin-top: 19px; text-align: left; }
  .expert-role { color: var(--orange); font-size: 12.5px; line-height: 15px; margin-top: 6px; text-align: left; }
  .expert p + p { margin-top: 14px; }
  .expert.nurse { display: flex; gap: 18px; margin-top: 22px; }
  .nurse .expert-photo { width: 77px; height: 94px; flex: none; background: linear-gradient(160deg, #d8d8d8, #9b8a78 60%, #6a5a4c); }
  .nurse .expert-name { margin-top: 2px; }
  .nurse .expert-role { margin-top: 3px; }
  .nurse p { margin-top: 16px; }

  /* Inside middle panel */
  .promise {
    position: absolute; left: 418px; width: 260px; top: 41px;
    color: var(--orange); font-size: 21px; line-height: 25.8px; text-align: center;
  }
  .photo-cross { position: absolute; left: 0; top: 0; }
  .brand-small { position: absolute; left: 433px; top: 708px; }
  .brand-name { font-family: "Montserrat", sans-serif; font-weight: 600; color: var(--navy); letter-spacing: -0.5px; line-height: 1; }
  .brand-small .brand-name { font-size: 28px; }
  .brand-tag { color: var(--grey-text); letter-spacing: 3.2px; text-transform: uppercase; }
  .brand-small .brand-tag { font-size: 10.5px; margin-top: 2px; }

  .contact { position: absolute; left: 433px; color: #444; font-size: 15px; line-height: 21px; display: flex; align-items: flex-start; gap: 6px; }
  .contact svg { flex: none; margin-top: 4px; }
  .contact.address { top: 767px; }
  .contact.phone { top: 828px; font-family: "Montserrat", sans-serif; font-weight: 700; font-size: 19px; line-height: 24px; color: #333; align-items: center; }
  .contact.phone svg { margin-top: 0; }
  .contact.email { top: 863px; }
  .contact.web { top: 890px; }
  .contact.email svg, .contact.web svg { margin-top: 5px; }
  .socials { position: absolute; left: 641px; top: 872px; display: flex; gap: 11px; }
  .socials span { width: 38px; height: 38px; border-radius: 50%; display: block; }
  .socials span:nth-child(1) { background: var(--navy); }
  .socials span:nth-child(2) { background: var(--blue); }
  .socials span:nth-child(3) { background: var(--orange); }

  /* Cover panel */
  .brand-cover { position: absolute; left: 920px; top: 196px; text-align: center; width: 260px; }
  .brand-cover .brand-name { font-size: 41px; }
  .brand-cover .brand-tag { font-size: 13.5px; letter-spacing: 4px; margin-top: 4px; }
  .greetings { position: absolute; right: 43px; top: 705px; text-align: right; }
  .greeting { display: block; white-space: nowrap; }
  .greeting.ko { font-family: "Noto Sans KR", sans-serif; font-weight: 300; font-size: 29px; color: #555; }
  .greeting.ja { font-family: "Noto Sans JP", sans-serif; font-size: 28px; color: var(--grey-text); margin-top: 14px; }
  .greeting.zh { font-family: "Noto Sans SC", sans-serif; font-weight: 500; font-size: 29px; color: var(--blue); margin-top: 12px; }
  .greeting.en { font-size: 30px; color: var(--orange); margin-top: 18px; }
</style>
</head>
<body>
<main class="brochure">

  <section class="experts" aria-label="Our health experts">
    <h2 class="experts-title">Our Health Experts</h2>

    <article class="expert">
      <div class="expert-card">
        <div class="expert-photo" role="img" aria-label="Portrait photo of Dr. D.H. Kwan"></div>
        <div class="expert-name">D.H. Kwan, MD, MBA</div>
        <div class="expert-role">Founder &amp;<br>Managing Director</div>
      </div>
      <p>D.H. Kwan, MD,MBA is a trained neurology physician and received MBA degree from Northfield University School of Business. His postgraduate medical training and academic appointments have included both clinical experience as a specialist in degenerative neurologic disease at Hanbit Medical School and executive manager as the medical director and director of the research center at Seorin Memorial Hospital in Korea. Dr. Kwan has several publications in various neurology journals and consulting experience in healthcare sector.</p>
    </article>

    <article class="expert">
      <div class="expert-card">
        <div class="expert-photo second" role="img" aria-label="Portrait photo of Dr. Robert E. Malden"></div>
        <div class="expert-name">Robert E. Malden<br>DO., MS.</div>
        <div class="expert-role">Founder &amp;<br>Managing Director</div>
      </div>
      <p>Robert Malden, DO, MS received his Doctor of Osteopathy (DO) from Lakeview State University College of Osteopathic Medicine (LSU-COM) and a Masters Degree in Clinical Research Design and Statistical Analysis from the University of Northfield School of Public Health. He did his internship at Brookmere Hospitals in Westport and served three years as a general medical officer in the United States Army, in eastern Bavaria, Germany and completed a residency in Emergency Medicine at Lakeview State University Affiliated Hospitals in Carlow City.</p>
      <p>He was an attending Emergency Medicine Physician at St. Aldric Hospital in Carlow City and was an assistant professor in Emergency Medicine at LSU-COM. In 1989 Dr. Malden took a position in Emergency Medicine at the University of Northfield Medical School (UNMS). He was active in clinical care, medical education, medical research and research regulatory compliance. His administrative positions have included Associate Chair for Research for the Department of Emergency Medicine, Assistant Dean for Research Regulatory Affairs at UNMS and Director of the Office of Human Research Compliance Review (OHRCR) in the Office of the Vice-President for Research. In July 2013, Dr. Malden retired from UN as a professor emeritus.</p>
    </article>

    <article class="expert nurse">
      <div class="expert-photo" role="img" aria-label="Portrait photo of nurse practitioner Martin Cho"></div>
      <div>
        <div class="expert-name">Martin Cho</div>
        <div class="expert-role">Nurse Practitioner</div>
        <p>BSN, MSN- Medical University of Southbrook; Board Certified Family Nurse Practitioner</p>
      </div>
    </article>
  </section>

  <p class="promise">We are staffed by<br>specially- trained<br>clinicians who provide<br>high- quality primary care<br>and can prescribe<br>appropriate medications.<br>They have advanced<br>degrees and clinical<br>training, and work<br>in partnership with<br>outstanding doctors.</p>

  <svg class="photo-cross" width="1200" height="937" viewBox="0 0 1200 937">
    <defs>
      <linearGradient id="g-desk" x1="0" y1="0" x2="1" y2="1"><stop offset="0" stop-color="#c9b49a"/><stop offset="0.6" stop-color="#ece9e4"/><stop offset="1" stop-color="#b9b4ad"/></linearGradient>
      <linearGradient id="g-visit" x1="0" y1="0" x2="1" y2="1"><stop offset="0" stop-color="#d9d2c7"/><stop offset="0.5" stop-color="#a9a99a"/><stop offset="1" stop-color="#c7bfb3"/></linearGradient>
      <linearGradient id="g-child" x1="0" y1="0" x2="1" y2="1"><stop offset="0" stop-color="#f1ece6"/><stop offset="0.5" stop-color="#c88a6c"/><stop offset="1" stop-color="#e9e6e2"/></linearGradient>
      <linearGradient id="g-team" x1="0" y1="0" x2="0" y2="1"><stop offset="0" stop-color="#f4f4f4"/><stop offset="0.5" stop-color="#8fb1c9"/><stop offset="1" stop-color="#e8eef2"/></linearGradient>
    </defs>
    <path d="M706 185 H893 Q906 185 906 198 V354 H1060 Q1073 354 1073 367 V557 Q1073 570 1060 570 H906 V727 Q906 740 893 740 H706 Q693 740 693 727 V570 H538 Q525 570 525 557 V367 Q525 354 538 354 H693 V198 Q693 185 706 185 Z"
          fill="#ffffff" stroke="var(--grey-frame)" stroke-width="15" stroke-linejoin="round"/>
    <rect x="707" y="204" width="184" height="132" fill="url(#g-desk)" role="img" aria-label="Photo of a billing statement with a pen and stethoscope"/>
    <rect x="544" y="369" width="274" height="187" fill="url(#g-visit)" role="img" aria-label="Photo of a young clinician talking with an older patient"/>
    <rect x="840" y="369" width="214" height="187" fill="url(#g-child)" role="img" aria-label="Photo of a doctor listening to a child with a stethoscope"/>
    <rect x="701" y="573" width="195" height="156" fill="url(#g-team)" role="img" aria-label="Photo of a medical team looking up"/>
  </svg>

  <div class="brand-small">
    <div class="brand-name">TOVANIX</div>
    <div class="brand-tag">Convenience Clinic</div>
  </div>

  <div class="contact address">
    <svg width="10" height="14" viewBox="0 0 10 14"><path d="M5 0C2.2 0 0 2.2 0 5c0 3.6 5 9 5 9s5-5.4 5-9c0-2.8-2.2-5-5-5zm0 7a2 2 0 110-4 2 2 0 010 4z" fill="var(--blue)"/></svg>
    <span>418 Linden Ave.<br>Maple Falls, OR 97000</span>
  </div>
  <div class="contact phone">
    <svg width="22" height="16" viewBox="0 0 22 16"><path d="M1 5C1 2 5 1 11 1s10 1 10 4v2h-5V5H6v2H1z" fill="var(--blue)"/><path d="M6 8h10l3 7H3z" fill="var(--blue)"/><circle cx="11" cy="11" r="2" fill="#fff"/></svg>
    <span>+1.555.014.2280</span>
  </div>
  <div class="contact email">
    <svg width="14" height="10" viewBox="0 0 14 10"><rect x="0.6" y="0.6" width="12.8" height="8.8" fill="none" stroke="var(--blue)" stroke-width="1.2"/><path d="M0.6 0.6L7 5.5l6.4-4.9" fill="none" stroke="var(--blue)" stroke-width="1.2"/></svg>
    <span>tovanixcare@mail.com</span>
  </div>
  <div class="contact web">
    <svg width="12" height="12" viewBox="0 0 12 12"><g fill="none" stroke="var(--blue)" stroke-width="1"><circle cx="6" cy="6" r="5.3"/><ellipse cx="6" cy="6" rx="2.3" ry="5.3"/><path d="M0.7 6h10.6M1.5 3.3h9M1.5 8.7h9"/></g></svg>
    <span>www.tova-nix.com</span>
  </div>
  <div class="socials" aria-label="Social media links"><span></span><span></span><span></span></div>

  <div class="brand-cover">
    <div class="brand-name">TOVANIX</div>
    <div class="brand-tag">Convenience Clinic</div>
  </div>

  <div class="greetings">
    <span class="greeting ko" lang="ko">편의 우리는 가치</span>
    <span class="greeting ja" lang="ja">利便性我々の価値</span>
    <span class="greeting zh" lang="zh">方便我们的价值</span>
    <span class="greeting en">Convenience We Value</span>
  </div>

  <div class="fold"></div>
  <div class="bottom-band"></div>
</main>
</body>
</html>
```